Small boutique multi-family apartment developer needs premium website design.

We are a growing real estate development company specializing in multi family apartment development. Our company Brindel Asset Development focuses on passive real estate investors looking to maximize their current real estate portfolio by allowing us to develop and reposition their current properties allowing them more cashflow while we are also able to take over the management of their asset in order to ensure optimal performance on a consistent basis.

```html
<!DOCTYPE html>
<html lang="en">
<head>
<meta charset="utf-8">
<title>Brindel Asset Development</title>
<link href="https://fonts.googleapis.com/css2?family=Poppins:wght@300;400;500&display=swap" rel="stylesheet">
<style>
:root{
  --navy:#091630;
  --navy-deep:#06102a;
  --band:#083a8f;
  --blue:#0d3b92;
  --accent:#1f9bff;
  --rose:#c6b0b0;
  --rose-text:#c9b1b1;
  --white:#ffffff;
  --field:#12223f;
  --muted:#5a6170;
}
*{margin:0;padding:0;box-sizing:border-box}
html,body{width:1200px;height:3776px;overflow:hidden}
body{background:var(--navy);font-family:'Poppins',sans-serif;color:var(--white);position:relative}
.abs{position:absolute}
.photo{position:absolute}
.btn{position:absolute;display:flex;align-items:center;justify-content:center;font-size:10px;letter-spacing:.5px;text-transform:uppercase;color:var(--navy)}
.btn.rose{background:var(--rose)}
.btn.white{background:var(--white)}
.btn .dash{display:inline-block;width:18px;height:2px;background:var(--navy);margin-right:10px}
.heading{font-weight:400;font-size:32px;line-height:44px}
.center{text-align:center;left:0;width:1200px}

/* header */
.logo{left:122px;top:20px;font-size:20px;font-weight:400}
.nav{top:25px;font-size:11px}
.nav.active{color:var(--accent)}
.contact-btn{left:968px;top:16px;width:109px;height:32px;border:2px solid var(--white);font-size:10px;display:flex;align-items:center;justify-content:center;text-transform:uppercase}
.contact-btn::before{content:"";width:12px;height:2px;background:var(--white);position:absolute;left:-2px;top:13px}

/* hero */
.hero{left:0;top:0;width:1200px;height:620px;background:linear-gradient(180deg,#163a7a 0%,#2e5fa6 30%,#4e7ab5 45%,#1b2f5a 68%,var(--navy) 100%)}
.welcome{top:108px;font-size:14px}
.welcome span{display:inline-block;width:58px;height:2px;background:var(--white);vertical-align:middle;margin:0 8px}
.hero-title{top:128px;font-size:50px;font-weight:400}
.hero-sub{top:186px;font-size:11px;line-height:15px}

/* about */
.eyebrow{left:119px;top:670px;font-size:18px;color:var(--rose-text)}
.eyebrow span{display:inline-block;width:66px;height:3px;background:var(--rose-text);vertical-align:middle;margin-left:8px}
.about-title{left:119px;top:693px;width:470px}
.about-text{left:119px;top:832px;width:385px;font-size:11px;line-height:18.7px}
.frame{border:4px solid var(--blue)}

/* services */
.card{position:absolute;background:var(--white);overflow:hidden}
.card .label{position:absolute;color:#1a1f2c}
.corner{position:absolute;right:0;bottom:0}

/* stats */
.stats{left:0;top:1460px;width:1200px;height:255px;background:var(--band)}
.stat-box{position:absolute;top:1522px;width:123px;height:108px;border:2px solid var(--white)}
.stat-num{position:absolute;left:0;width:123px;bottom:4px;text-align:center;font-size:40px;font-weight:400}
.stat-label{position:absolute;top:1641px;width:200px;text-align:center;font-size:18px}
.divider{position:absolute;top:1528px;width:1px;height:108px;background:rgba(255,255,255,.35)}

/* projects */
.proj-title{font-size:15px;color:#1a1f2c;position:absolute;left:12px;top:6px}
.proj-text{font-size:10px;color:var(--muted);position:absolute;left:12px;top:28px;line-height:14px}

/* contact */
.field{position:absolute;left:724px;width:353px;background:var(--field);font-size:11px;padding:10px 12px}

/* footer */
.foot-head{font-size:16px;position:absolute}
.foot-link{font-size:9px;position:absolute}
.foot-div{position:absolute;top:3586px;width:1px;height:158px;background:rgba(255,255,255,.35)}
</style>
</head>
<body>

<!-- hero -->
<div class="photo hero" role="img" aria-label="Harbor skyline with high-rise towers and a marina of yachts at dusk"></div>
<div class="abs logo">Brindel Asset Development</div>
<div class="abs nav active" style="left:622px">Home</div>
<div class="abs nav" style="left:708px">About Us</div>
<div class="abs nav" style="left:808px">Projects</div>
<div class="abs nav" style="left:904px">News</div>
<div class="abs contact-btn">Contact Us</div>

<div class="abs center welcome"><span></span>Welcome To<span></span></div>
<div class="abs center hero-title">Brindel Asset Development</div>
<div class="abs center hero-sub">Lorem ipsum dolor sit amet, consectetur adipiscing elit,<br>sed do eiusmod tempor incididunt ut labore et dolore magna aliqua.</div>
<div class="btn white" style="left:545px;top:229px;width:110px;height:32px"><span class="dash"></span>Get Started</div>

<!-- about -->
<div class="abs eyebrow">About Us<span></span></div>
<div class="abs heading about-title">Committed to the fundamentals of Investing, to ensure longterm growth</div>
<p class="abs about-text">Brindel Asset Development was created to satisfy the overwhelming request to help our clients who want to invest in long term buy and hold Real Estate, and create a more profitable and balanced investment portfolio. We offer opportunities to invest in cash flowing Multi-Family apartment building investments in the Southern California area.</p>
<div class="btn rose" style="left:119px;top:965px;width:112px;height:35px"><span class="dash"></span>Read More</div>
<div class="abs frame" style="left:678px;top:659px;width:399px;height:355px"></div>
<div class="photo" role="img" aria-label="Glass office towers with potted plants and a rising growth arrow" style="left:694px;top:677px;width:365px;height:322px;background:linear-gradient(160deg,#9fc8ea,#3f7fb8 45%,#3d6b3f 85%)"></div>

<!-- services -->
<div class="abs heading center" style="top:1066px">Committed to the fundamentals of<br>Investing, to ensure longterm growth</div>

<div class="card" style="left:122px;top:1173px;width:310px;height:230px">
  <div class="photo" role="img" aria-label="Engineer with a tablet in front of an apartment building" style="left:0;top:0;width:310px;height:162px;background:linear-gradient(120deg,#c9ccd2,#9aa7b6 55%,#c97b52)"></div>
  <div class="label" style="left:19px;top:174px;font-size:18px;line-height:22px">Apartment Building<br>Optimization</div>
  <svg class="corner" width="42" height="42" viewBox="0 0 42 42"><polygon points="42,0 42,42 0,42" fill="#0d3b92"/><path d="M22 33h14M31 29l5 4-5 4" stroke="#fff" stroke-width="1.3" fill="none"/></svg>
</div>
<div class="card" style="left:444px;top:1173px;width:310px;height:230px">
  <div class="photo" role="img" aria-label="Desk with a monitor showing real estate charts and a man working" style="left:0;top:0;width:310px;height:162px;background:linear-gradient(120deg,#5d6e82,#b7c0c9 55%,#e7e3dd)"></div>
  <div class="label" style="left:19px;top:174px;font-size:18px;line-height:22px">Real Estate Portfolio<br>Management</div>
  <svg class="corner" width="42" height="42" viewBox="0 0 42 42"><polygon points="42,0 42,42 0,42" fill="#0d3b92"/><path d="M22 33h14M31 29l5 4-5 4" stroke="#fff" stroke-width="1.3" fill="none"/></svg>
</div>
<div class="card" style="left:766px;top:1173px;width:311px;height:230px">
  <div class="photo" role="img" aria-label="Handshake over a signed agreement" style="left:0;top:0;width:311px;height:162px;background:linear-gradient(120deg,#6f6a52,#c4b8a4 50%,#dfe3e6)"></div>
  <div class="label" style="left:19px;top:174px;font-size:18px;line-height:22px">Private Lending</div>
  <svg class="corner" width="42" height="42" viewBox="0 0 42 42"><polygon points="42,0 42,42 0,42" fill="#0d3b92"/><path d="M22 33h14M31 29l5 4-5 4" stroke="#fff" stroke-width="1.3" fill="none"/></svg>
</div>

<!-- stats -->
<div class="abs stats"></div>
<div class="stat-box" style="left:122px">
  <svg class="abs" style="left:38px;top:10px" width="46" height="36" viewBox="0 0 46 36" fill="none" stroke="#fff" stroke-width="1.8"><path d="M6 18l10-10 8 4 8-4 10 10-14 12-4-4-4 4z"/><path d="M16 8l10 10"/></svg>
  <div class="stat-num">02</div>
</div>
<div class="stat-label" style="left:83px">Partners</div>
<div class="divider" style="left:328px"></div>

<div class="stat-box" style="left:400px">
  <svg class="abs" style="left:40px;top:8px" width="42" height="38" viewBox="0 0 42 38" fill="none" stroke="#fff" stroke-width="1.8"><circle cx="21" cy="10" r="5"/><path d="M12 34V22a9 9 0 0 1 18 0v12"/><path d="M6 20v-8M36 20v-8"/></svg>
  <div class="stat-num">06</div>
</div>
<div class="stat-label" style="left:361px">Employees</div>
<div class="divider" style="left:599px"></div>

<div class="stat-box" style="left:680px">
  <svg class="abs" style="left:38px;top:8px" width="46" height="38" viewBox="0 0 46 38" fill="none" stroke="#fff" stroke-width="1.8"><rect x="4" y="14" width="12" height="22"/><rect x="18" y="6" width="12" height="30"/><circle cx="36" cy="24" r="7"/></svg>
  <div class="stat-num">33</div>
</div>
<div class="stat-label" style="left:641px">Investments</div>
<div class="divider" style="left:875px"></div>

<div class="stat-box" style="left:954px">
  <svg class="abs" style="left:40px;top:8px" width="42" height="38" viewBox="0 0 42 38" fill="none" stroke="#fff" stroke-width="1.8"><path d="M13 4h16v10a8 8 0 0 1-16 0z"/><path d="M13 8H7a6 6 0 0 0 6 8M29 8h6a6 6 0 0 1-6 8"/><path d="M21 22v6M13 34h16"/></svg>
  <div class="stat-num">100%</div>
</div>
<div class="stat-label" style="left:915px">Success</div>

<!-- projects -->
<div class="abs heading center" style="top:1759px">Our Projects</div>

<div class="card" style="left:125px;top:1824px;width:303px;height:220px">
  <div class="photo" role="img" aria-label="Terraced apartment complex with balconies" style="left:0;top:0;width:303px;height:160px;background:linear-gradient(180deg,#7fa3c4,#b9a58e 60%,#6d5a48)"></div>
  <div class="abs" style="left:0;top:160px;width:260px;height:60px;background:#fff"><div class="proj-title">Projects 1</div><div class="proj-text">Our mixed-use developments for<br>communities to live, work &amp; play</div></div>
  <svg class="corner" width="42" height="42" viewBox="0 0 42 42"><polygon points="42,0 42,42 0,42" fill="#0d3b92"/><path d="M22 33h14M31 29l5 4-5 4" stroke="#fff" stroke-width="1.3" fill="none"/></svg>
</div>
<div class="card" style="left:448px;top:1824px;width:304px;height:220px">
  <div class="photo" role="img" aria-label="Modern residential towers and villas around a pool" style="left:0;top:0;width:304px;height:160px;background:linear-gradient(180deg,#aebccb,#6f8a79 55%,#3f4b3c)"></div>
  <div class="abs" style="left:0;top:160px;width:260px;height:60px;background:#fff"><div class="proj-title">Projects 2</div><div class="proj-text">Our mixed-use developments for<br>communities to live, work &amp; play</div></div>
  <svg class="corner" width="42" height="42" viewBox="0 0 42 42"><polygon points="42,0 42,42 0,42" fill="#0d3b92"/><path d="M22 33h14M31 29l5 4-5 4" stroke="#fff" stroke-width="1.3" fill="none"/></svg>
</div>
<div class="card" style="left:773px;top:1824px;width:304px;height:220px">
  <div class="photo" role="img" aria-label="Bright kitchen interior with wood ceiling" style="left:0;top:0;width:304px;height:160px;background:linear-gradient(180deg,#b0794a,#e6e3de 40%,#cfc8bf)"></div>
  <div class="abs" style="left:0;top:160px;width:260px;height:60px;background:#fff"><div class="proj-title">Projects 3</div><div class="proj-text">Our mixed-use developments for<br>communities to live, work &amp; play</div></div>
  <svg class="corner" width="42" height="42" viewBox="0 0 42 42"><polygon points="42,0 42,42 0,42" fill="#0d3b92"/><path d="M22 33h14M31 29l5 4-5 4" stroke="#fff" stroke-width="1.3" fill="none"/></svg>
</div>
<div class="card" style="left:125px;top:2064px;width:303px;height:219px">
  <div class="photo" role="img" aria-label="Open living room with wood ceiling" style="left:0;top:0;width:303px;height:159px;background:linear-gradient(180deg,#a8744a,#eeeae4 40%,#d4d0ca)"></div>
  <div class="abs" style="left:0;top:159px;width:260px;height:60px;background:#fff"><div class="proj-title">Projects 4</div><div class="proj-text">Our mixed-use developments for<br>communities to live, work &amp; play</div></div>
  <svg class="corner" width="42" height="42" viewBox="0 0 42 42"><polygon points="42,0 42,42 0,42" fill="#0d3b92"/><path d="M22 33h14M31 29l5 4-5 4" stroke="#fff" stroke-width="1.3" fill="none"/></svg>
</div>
<div class="card" style="left:448px;top:2064px;width:304px;height:219px">
  <div class="photo" role="img" aria-label="Modern house exterior at twilight" style="left:0;top:0;width:304px;height:159px;background:linear-gradient(180deg,#1d3a78,#4a5a78 50%,#2a2d33)"></div>
  <div class="abs" style="left:0;top:159px;width:260px;height:60px;background:#fff"><div class="proj-title">Projects 5</div><div class="proj-text">Our mixed-use developments for<br>communities to live, work &amp; play</div></div>
  <svg class="corner" width="42" height="42" viewBox="0 0 42 42"><polygon points="42,0 42,42 0,42" fill="#0d3b92"/><path d="M22 33h14M31 29l5 4-5 4" stroke="#fff" stroke-width="1.3" fill="none"/></svg>
</div>
<div class="card" style="left:773px;top:2064px;width:304px;height:219px">
  <div class="photo" role="img" aria-label="Modern house with lit garage at dusk" style="left:0;top:0;width:304px;height:159px;background:linear-gradient(180deg,#1c4fa0,#8a8a8c 55%,#3a3633)"></div>
  <div class="abs" style="left:0;top:159px;width:260px;height:60px;background:#fff"><div class="proj-title">Projects 6</div><div class="proj-text">Our mixed-use developments for<br>communities to live, work &amp; play</div></div>
  <svg class="corner" width="42" height="42" viewBox="0 0 42 42"><polygon points="42,0 42,42 0,42" fill="#0d3b92"/><path d="M22 33h14M31 29l5 4-5 4" stroke="#fff" stroke-width="1.3" fill="none"/></svg>
</div>
<div class="btn rose" style="left:532px;top:2310px;width:135px;height:35px"><span class="dash"></span>View All Project</div>

<!-- contact -->
<div class="abs frame" style="left:122px;top:2461px;width:490px;height:364px"></div>
<div class="photo" role="img" aria-label="Hands sketching plans on paper beside a laptop" style="left:142px;top:2482px;width:450px;height:322px;background:linear-gradient(150deg,#c8d3d8,#9fb3ba 50%,#586067)"></div>
<div class="abs heading" style="left:719px;top:2469px">For any inquiries,<br>please call or email us.</div>
<div class="abs" style="left:722px;top:2560px;font-size:12px">Alternatively you can fill in the following contact form.</div>
<div class="field" style="top:2594px;height:34px">Name</div>
<div class="field" style="top:2643px;height:34px">Email</div>
<div class="field" style="top:2691px;height:73px">Message</div>
<div class="btn white" style="left:722px;top:2778px;width:98px;height:35px"><span class="dash"></span>Submit</div>

<!-- news -->
<div class="abs heading" style="left:122px;top:2869px">Latest News</div>
<div class="btn rose" style="left:939px;top:2873px;width:139px;height:35px"><span class="dash"></span>View All News</div>

<div class="card" style="left:122px;top:2940px;width:468px;height:299px;background:transparent">
  <div class="photo" role="img" aria-label="Modern house with lit terrace at twilight" style="left:0;top:0;width:468px;height:299px;background:linear-gradient(180deg,#1d4a9a,#5a6478 55%,#2b2c30)"></div>
  <div class="abs" style="left:0;top:236px;width:304px;height:63px;background:#fff;color:#1a1f2c">
    <div class="abs" style="left:18px;top:10px;font-size:10px;color:var(--blue);text-decoration:underline">Feb 20, 2022</div>
    <div class="abs" style="left:14px;top:26px;font-size:15px">Bold and Breathtaking</div>
  </div>
</div>
<div class="card" style="left:609px;top:2940px;width:468px;height:299px;background:transparent">
  <div class="photo" role="img" aria-label="Kitchen interior with wood ceiling and pendant light" style="left:0;top:0;width:468px;height:299px;background:linear-gradient(180deg,#a9734a,#ecebe7 40%,#b9b3aa 80%,#2c2d31)"></div>
  <div class="abs" style="left:0;top:236px;width:304px;height:63px;background:#fff;color:#1a1f2c">
    <div class="abs" style="left:18px;top:10px;font-size:10px;color:var(--blue);text-decoration:underline">Feb 20, 2022</div>
    <div class="abs" style="left:14px;top:26px;font-size:15px">Bold and Breathtaking</div>
  </div>
</div>

<!-- call to action -->
<div class="abs" style="left:0;top:3302px;width:1200px;height:259px;background:var(--rose)"></div>
<div class="abs heading center" style="top:3343px">Start Your New Journey<br>with Brindel Asset Development</div>
<div class="abs center" style="top:3430px;font-size:10.5px;line-height:15px">Lorem ipsum dolor sit amet, consectetur adipiscing elit, sed do eiusmod tempor<br>incididunt ut labore et dolore magna aliqua. Quis ipsum suspendisse ultrices gravida.</div>
<div class="btn white" style="left:510px;top:3473px;width:179px;height:36px"><span class="dash"></span>Start Your Journey</div>

<!-- footer -->
<div class="abs" style="left:0;top:3561px;width:1200px;height:215px;background:var(--navy-deep)"></div>
<div class="foot-head" style="left:122px;top:3592px">Brindel Asset Development</div>
<p class="abs" style="left:122px;top:3632px;width:225px;font-size:8.5px;line-height:18px">Brindel Asset Development was created to satisfy the overwhelming request to help our clients who want to invest in long term buy and hold Real Estate, and create a more profitable and balanced investment portfolio.</p>
<div class="foot-div" style="left:388px"></div>

<div class="foot-head" style="left:478px;top:3584px">About Us</div>
<div class="foot-link" style="left:478px;top:3622px">Home</div>
<div class="foot-link" style="left:478px;top:3642px">About Us</div>
<div class="foot-link" style="left:478px;top:3662px">Projects</div>
<div class="foot-link" style="left:478px;top:3683px">News</div>
<div class="foot-link" style="left:478px;top:3703px">Contact Us</div>
<div class="foot-div" style="left:633px"></div>

<div class="foot-head" style="left:699px;top:3584px">Contact Us</div>
<svg class="abs" style="left:700px;top:3620px" width="18" height="18" viewBox="0 0 18 18" fill="none" stroke="#fff" stroke-width="1"><circle cx="9" cy="9" r="8"/><path d="M9 14s-4-4-4-6.5a4 4 0 0 1 8 0C13 10 9 14 9 14z"/><circle cx="9" cy="7.5" r="1.3"/></svg>
<div class="foot-link" style="left:726px;top:3621px;line-height:12px">1480 Harbor View Ave Suite 310<br>Seaport, CA, 90412</div>
<svg class="abs" style="left:700px;top:3655px" width="18" height="18" viewBox="0 0 18 18" fill="none" stroke="#fff" stroke-width="1"><circle cx="9" cy="9" r="8"/><rect x="5" y="6" width="8" height="6"/><path d="M5 6l4 3 4-3"/></svg>
<div class="foot-link" style="left:726px;top:3659px">info@brindelassets.com</div>
<svg class="abs" style="left:700px;top:3690px" width="18" height="18" viewBox="0 0 18 18" fill="none" stroke="#fff" stroke-width="1"><circle cx="9" cy="9" r="8"/><path d="M6 5l2 0 1 2.5-1.2 1a5 5 0 0 0 2.7 2.7l1-1.2 2.5 1v2a1 1 0 0 1-1 1A8 8 0 0 1 5 6a1 1 0 0 1 1-1z"/></svg>
<div class="foot-link" style="left:726px;top:3694px">+ (555) 014-2290</div>
<div class="foot-div" style="left:920px"></div>

<div class="foot-head" style="left:996px;top:3584px">Follow Us</div>
<svg class="abs" style="left:997px;top:3620px" width="18" height="18"><circle cx="9" cy="9" r="8" fill="none" stroke="#fff"/></svg>
<div class="foot-link" style="left:1023px;top:3624px">Pageboard</div>
<svg class="abs" style="left:997px;top:3651px" width="18" height="18"><circle cx="9" cy="9" r="8" fill="none" stroke="#fff"/></svg>
<div class="foot-link" style="left:1023px;top:3655px">Worklink</div>
<svg class="abs" style="left:997px;top:3682px" width="18" height="18"><circle cx="9" cy="9" r="8" fill="none" stroke="#fff"/></svg>
<div class="foot-link" style="left:1023px;top:3686px">Chirpline</div>

<div class="abs center" style="top:3753px;font-size:8px">© 2024 Brindel Asset Development All Rights Reserved</div>
</body>
</html>
```